Business Card Design

Electrical Contracting buisness
need a buisness card relating to that buisness

Reason: Just need to discuss with partner

Industry/Entity Type

Business

Contact Information for Business Card

Colin Harbage Electrical
0417 562 983
colinharbage7@mailvessel.com
REC 48761

```html
<!DOCTYPE html>
<html lang="en">
<head>
<meta charset="utf-8">
<title>Colin Harbage Electrical – Business Card</title>
<link rel="stylesheet" href="https://fonts.googleapis.com/css2?family=Arimo:wght@400;700&display=swap">
<style>
  :root {
    --backdrop: #e6e6e6;
    --card: #ffffff;
    --brand-grey: #5f5f5f;
    --brand-grey-light: #9a9a9a;
    --text-grey: #7a7a7a;
    --ink: #1e1e1e;
    --wire-teal: #1aa58e;
    --wire-teal-light: #5fd0bb;
    --brass: #d8c27a;
  }
  html, body {
    margin: 0;
    padding: 0;
    width: 1200px;
    height: 900px;
    overflow: hidden;
    background: var(--backdrop);
  }
  .canvas {
    position: relative;
    width: 1200px;
    height: 900px;
    font-family: "Arimo", Arial, sans-serif;
  }
  .business-card {
    position: absolute;
    left: 105px;
    top: 150px;
    width: 990px;
    height: 600px;
    background: var(--card);
    box-shadow: 0 6px 24px rgba(0,0,0,0.18);
    overflow: hidden;
  }
  .wire-artwork {
    position: absolute;
    left: 540px;
    top: 110px;
    width: 300px;
    height: 320px;
    background: radial-gradient(ellipse at 60% 45%, var(--wire-teal) 0%, var(--wire-teal-light) 45%, rgba(216,194,122,0.6) 70%, rgba(255,255,255,0) 100%);
  }
  .company-name {
    position: absolute;
    left: 70px;
    top: 52px;
    margin: 0;
    font-size: 42px;
    font-weight: 700;
    letter-spacing: 0.5px;
    color: var(--brand-grey);
    white-space: nowrap;
  }
  .person {
    position: absolute;
    left: 110px;
    top: 150px;
  }
  .person-name {
    margin: 0;
    font-size: 26px;
    font-weight: 700;
    color: var(--text-grey);
    letter-spacing: 1px;
  }
  .person-role {
    margin: 2px 0 0 8px;
    font-size: 13px;
    font-weight: 700;
    color: var(--text-grey);
    letter-spacing: 1.5px;
  }
  .licence {
    position: absolute;
    right: 24px;
    top: 255px;
    margin: 0;
    font-size: 22px;
    font-weight: 700;
    color: var(--ink);
    letter-spacing: 0.5px;
  }
  .contact {
    position: absolute;
    left: 70px;
    bottom: 60px;
    font-size: 32px;
    color: var(--text-grey);
    line-height: 1.2;
  }
  .contact p { margin: 0; }
</style>
</head>
<body>
<main class="canvas">
  <section class="business-card">
    <div class="wire-artwork" role="img" aria-label="Photograph of teal electrical cables with brass spade terminals fanning out"></div>
    <h1 class="company-name">Colin Harbage Electrical</h1>
    <div class="person">
      <p class="person-name">DANIEL PRESCOTT</p>
      <p class="person-role">GENERAL MANEGER</p>
    </div>
    <p class="licence">REC 48761</p>
    <div class="contact">
      <p class="contact-phone">0417 562 983</p>
      <p class="contact-email">colinharbage7@mailvessel.com</p>
    </div>
  </section>
</main>
</body>
</html>
```